brochure for high-end senior living company

We need a new brochure that we can pass out to doctors and social workers so they would choose us over the competition.
brightmeadowhaven.example is our website that shows our colors and themes

we stand out over our competition due to our high quality of staff and our staff to resident ratio.
We are not afraid of difficult and complex care situations. Instead, we thrive on coordinating complexity.

We do all of this in a lovely setting that is luxurious and feels like home.

Target Market(s)

The families who make the decision are 60-70 years old. They are not not "rich" but they have saved well and usually have more than 1 million in assets.

Industry/Entity Type

Senior Living, Memory Care

Font styles to use
Serif

Colors
00AB8E
00BBA5
67D7C9
C6EFE9
E9F9F6
FFC000
F8CF3A
FAE287
FDF2CF
FEFAEE

Requirements
Must have
• When compromise is not an option...
Nice to have
• A difficult balance of beautiful and activities (happy people), but also communicating that we handle difficult and complex care.

```html
<!DOCTYPE html>
<html lang="en">
<head>
<meta charset="utf-8">
<title>Bright Meadow Haven – Trifold Brochure</title>
<link rel="stylesheet" href="https://fonts.googleapis.com/css2?family=Ubuntu:wght@500&family=Roboto:wght@300;400&family=Great+Vibes&family=Crimson+Text:wght@400&display=swap">
<style>
  :root {
    --teal: #3bb39a;
    --teal-deep: #00ab8e;
    --teal-soft: #c6efe9;
    --gold: #d9b45a;
    --gold-pill: #e0c173;
    --ink: #3c3c3c;
    --ink-soft: #555;
    --brand-ink: #2f5c5a;
    --paper: #ffffff;
    --backdrop: #f0f0ee;
  }
  * { box-sizing: border-box; margin: 0; padding: 0; }
  html, body { width: 1200px; height: 900px; overflow: hidden; background: var(--backdrop); }
  .brochure {
    position: absolute; left: 75px; top: 22px; width: 1050px; height: 855px;
    background: var(--paper); box-shadow: 0 4px 18px rgba(0,0,0,.12); overflow: hidden;
    font-family: "Roboto", Arial, sans-serif; color: var(--ink);
  }
  .panel { position: absolute; top: 0; width: 350px; height: 855px; }
  .panel--about { left: 0; }
  .panel--services { left: 350px; }
  .panel--cover { left: 700px; }
  .fold { position: absolute; top: 0; width: 1px; height: 855px; background: rgba(0,0,0,.06); z-index: 5; }

  .section-title {
    font-family: "Ubuntu", sans-serif; font-weight: 500; color: var(--teal);
    font-size: 31px; line-height: 1; position: absolute; left: 34px;
  }
  .section-title::after {
    content: ""; position: absolute; left: 0; bottom: -8px; width: 210px; height: 2px;
    background: var(--gold); box-shadow: 0 3px 0 -1px var(--teal);
  }
  .panel--about .section-title { top: 32px; }
  .panel--services .section-title { top: 22px; left: 35px; font-size: 32px; }
  .panel--services .section-title::after { width: 150px; }

  .subtitle { position: absolute; left: 34px; font-weight: 300; font-size: 14px; color: var(--ink-soft); }
  .panel--about .subtitle { top: 72px; }
  .panel--services .subtitle { top: 72px; left: 36px; width: 250px; line-height: 17px; font-size: 13.5px; }

  .info-box {
    position: absolute; left: 34px; top: 99px; width: 310px; height: 316px;
    border: 2px solid var(--teal); border-radius: 14px; overflow: hidden;
  }
  .info-box__head {
    background: var(--teal); color: #fff; font-size: 12px; padding: 3px 12px; height: 20px;
  }
  .info-box__head:first-child { height: 30px; padding-top: 10px; }
  .info-box__text { font-size: 7.4px; line-height: 11px; padding: 6px 12px 8px; color: var(--ink-soft); }

  .photo { position: absolute; }
  .photo--house {
    left: 0; top: 400px; width: 700px; height: 370px;
    background: linear-gradient(180deg, #f3f3f1 0%, #dfe3dc 30%, #b7a590 55%, #e6dcc0 70%, #c9c9c4 85%, #d8d6d0 100%);
  }
  .photo--patio {
    left: 700px; top: 60px; width: 350px; height: 560px;
    background: linear-gradient(180deg, #eef2ea 0%, #9bb07a 25%, #c9b9a6 45%, #7f9a58 70%, #b9bdb2 100%);
  }
  .overlay { position: absolute; left: 0; top: 0; width: 1050px; height: 855px; z-index: 2; }

  .care-list { position: absolute; left: 36px; top: 112px; list-style: none; }
  .care-list li {
    font-size: 10.5px; font-weight: 300; color: var(--ink-soft); height: 19.5px;
    display: flex; align-items: center; gap: 10px;
  }
  .care-list svg { width: 14px; height: 14px; flex: none; }

  .contact { position: absolute; right: 25px; top: 660px; text-align: right; z-index: 3; }
  .contact__phone {
    display: inline-flex; align-items: center; background: var(--gold-pill); color: #fff;
    border-radius: 10px; height: 19px; padding: 0 12px 0 0; font-size: 14px; margin-bottom: 6px;
  }
  .contact__phone svg { width: 20px; height: 20px; margin-right: 10px; }
  .contact__line {
    font-size: 13px; font-weight: 300; color: var(--ink); line-height: 19px;
    border-bottom: 1px solid var(--gold); display: inline-block;
  }

  .thumbs { position: absolute; left: 24px; top: 755px; display: flex; gap: 10px; z-index: 3; }
  .thumb { height: 74px; }
  .thumb--activity { width: 96px; background: linear-gradient(135deg, #3a2c1d, #a9793c 60%, #e2c27a); }
  .thumb--outing { width: 86px; background: linear-gradient(135deg, #9eb6c6, #c9b6a3 50%, #6d8c55); }
  .thumb--lounge { width: 97px; background: linear-gradient(135deg, #f1ead8, #d9c39b 60%, #a68a62); }

  .tagline {
    position: absolute; left: 24px; top: 26px; font-family: "Great Vibes", cursive;
    color: var(--teal); font-size: 24px;
  }
  .brand { position: absolute; text-align: center; z-index: 3; font-family: "Crimson Text", serif; color: var(--brand-ink); }
  .brand__name { font-size: 36px; line-height: 1; display: block; border-bottom: 1px solid var(--gold); padding-bottom: 6px; }
  .brand__sub { font-size: 22px; display: block; padding-top: 6px; }
  .panel--cover .brand { left: 20px; width: 310px; top: 660px; }
  .panel--about .brand { left: 140px; width: 190px; top: 775px; }
  .panel--about .brand__name { font-size: 20px; padding-bottom: 4px; }
  .panel--about .brand__sub { font-size: 13px; padding-top: 3px; }
</style>
</head>
<body>
<div class="brochure">
  <div class="photo photo--house" role="img" aria-label="Photo of the single-storey stone and siding residence with flag pole and driveway"></div>
  <div class="photo photo--patio" role="img" aria-label="Photo of residents and family gathered around a table on a covered patio beside a lawn"></div>

  <svg class="overlay" viewBox="0 0 1050 855" aria-hidden="true">
    <polygon points="0,755 700,572 700,855 0,855" fill="#fff"/>
    <polygon points="0,744 700,562 700,573 0,757" fill="#3bb39a"/>
    <path d="M700,585 L880,532 Q900,526 918,534 L1050,590 L1050,855 L700,855 Z" fill="#fff"/>
    <path d="M700,573 L880,520 Q900,514 918,522 L1050,578 L1050,590 L918,534 Q900,526 880,532 L700,585 Z" fill="#3bb39a"/>
  </svg>
  <div class="fold" style="left:350px"></div>
  <div class="fold" style="left:700px"></div>

  <section class="panel panel--about">
    <h1 class="section-title">About Us</h1>
    <p class="subtitle">Around the Clock Quality Care for Your Loved One.</p>
    <div class="info-box">
      <div class="info-box__head">What We Do</div>
      <p class="info-box__text">In America, people aren't used to assistance. We love independence and freedom and don't plan on giving them up. At Bright Meadow Haven Residential Assisted Living, we get that. When a person comes through our doors and needs to transition to more assistance, we work very hard to make it painless and, dare we say, enjoyable! We come alongside strong independent people and offer gentle, patient, and friendly help.</p>
      <div class="info-box__head">Why We Do</div>
      <p class="info-box__text">Being in assisted living such a long time, we saw the spectrum of care that exists out there. We saw a need for higher acuity care. So we set out to find the sweet balance of high quality care combined with a home atmosphere. We do that through a three-pronged method. First, we partner with licensed medical help every step of the way. Second, we hire CNAs, medical assistants, and nurses on their way to becoming registered. Third, we only choose homes that are spacious and inviting. We believe this balance accomplishes our</p>
      <div class="info-box__head">Why We're Residential</div>
      <p class="info-box__text">The residential assisted living model allows us to keep the caregiver to resident ratio small. Simply put, the more residents, the more the caregivers are spread thin. In our environment we can achieve what we believe is the ideal ratio. We are also able to get to know every resident very closely. This is great relationally, but it's also medically advantages since we are able to quickly assess a change in medical condition.</p>
    </div>
    <div class="brand"><span class="brand__name">Bright Meadow Haven</span><span class="brand__sub">Residential Assisted Living</span></div>
  </section>

  <section class="panel panel--services">
    <h2 class="section-title">Service We Provide</h2>
    <p class="subtitle">Our Senior Living staff provides numerous specialized care services!</p>
    <ul class="care-list">
      <li><svg viewBox="0 0 14 14"><rect x="1" y="3" width="10" height="10" fill="none" stroke="#3bb39a" stroke-width="1.5"/><path d="M3 7 L6 10 L13 1" fill="none" stroke="#3bb39a" stroke-width="2"/></svg>Alzheimer's &amp; Dementia Care</li>
      <li><svg viewBox="0 0 14 14"><rect x="1" y="3" width="10" height="10" fill="none" stroke="#3bb39a" stroke-width="1.5"/><path d="M3 7 L6 10 L13 1" fill="none" stroke="#3bb39a" stroke-width="2"/></svg>Stroke Care</li>
      <li><svg viewBox="0 0 14 14"><rect x="1" y="3" width="10" height="10" fill="none" stroke="#3bb39a" stroke-width="1.5"/><path d="M3 7 L6 10 L13 1" fill="none" stroke="#3bb39a" stroke-width="2"/></svg>Parkinson's Care</li>
      <li><svg viewBox="0 0 14 14"><rect x="1" y="3" width="10" height="10" fill="none" stroke="#3bb39a" stroke-width="1.5"/><path d="M3 7 L6 10 L13 1" fill="none" stroke="#3bb39a" stroke-width="2"/></svg>Limited Mobility</li>
      <li><svg viewBox="0 0 14 14"><rect x="1" y="3" width="10" height="10" fill="none" stroke="#3bb39a" stroke-width="1.5"/><path d="M3 7 L6 10 L13 1" fill="none" stroke="#3bb39a" stroke-width="2"/></svg>Hospice Care</li>
      <li><svg viewBox="0 0 14 14"><rect x="1" y="3" width="10" height="10" fill="none" stroke="#3bb39a" stroke-width="1.5"/><path d="M3 7 L6 10 L13 1" fill="none" stroke="#3bb39a" stroke-width="2"/></svg>Skin &amp; Incontinence Care</li>
      <li><svg viewBox="0 0 14 14"><rect x="1" y="3" width="10" height="10" fill="none" stroke="#3bb39a" stroke-width="1.5"/><path d="M3 7 L6 10 L13 1" fill="none" stroke="#3bb39a" stroke-width="2"/></svg>Short Term Stays</li>
    </ul>
    <address class="contact" style="font-style:normal">
      <div class="contact__phone"><svg viewBox="0 0 20 20"><circle cx="10" cy="10" r="10" fill="#3bb39a"/><path d="M7 5 L9 8 L8 9 Q9 11.5 11 12 L12 11 L15 13 L13.5 15 Q8 15 5 7 Z" fill="#fff"/></svg>555-014-2276</div><br>
      <span class="contact__line">1420 Larkspur Lane</span><br>
      <span class="contact__line">Fairbrook, CA 90210</span><br>
      <span class="contact__line">www.brightmeadowhaven.example</span>
    </address>
    <div class="thumbs">
      <div class="thumb thumb--activity" role="img" aria-label="Photo of residents playing a floor game indoors"></div>
      <div class="thumb thumb--outing" role="img" aria-label="Photo of an outdoor gathering beside a food truck"></div>
      <div class="thumb thumb--lounge" role="img" aria-label="Photo of a bright furnished living room"></div>
    </div>
  </section>

  <section class="panel panel--cover">
    <p class="tagline">When compromise is not an option...</p>
    <div class="brand"><span class="brand__name">Bright Meadow Haven</span><span class="brand__sub">Residential Assisted Living</span></div>
  </section>
</div>
</body>
</html>
```